amber crest health and wellness group.

need a full website design , all information provided in word document labeled website blue print

Target Market(s)

first responders, military , people in crisis

Coding

Coded - Design and coding required

Number of Pages Required

1 page

```html
<!DOCTYPE html>
<html lang="en">
<head>
<meta charset="utf-8">
<title>Amber Crest Health &amp; Wellness Group</title>
<link href="https://fonts.googleapis.com/css2?family=Italiana&family=Lato:wght@400;700&display=swap" rel="stylesheet">
<style>
:root{
  --blue:#2f6fc0;
  --blue-bright:#3d8ee8;
  --blue-deep:#1d4f95;
  --navy:#12305c;
  --ink:#1d1d1d;
  --muted:#555;
  --black:#000;
  --white:#fff;
  --card-shadow:0 4px 18px rgba(0,0,0,.12);
}
*{margin:0;padding:0;box-sizing:border-box}
html,body{width:1200px;height:4383px;overflow:hidden}
body{position:relative;background:var(--white);font-family:'Lato',sans-serif;color:var(--ink)}
.abs{position:absolute}
.display{font-family:'Italiana',serif;font-weight:400}
.btn{position:absolute;display:flex;align-items:center;justify-content:center;border-radius:16px;font-size:10px;font-weight:700;letter-spacing:.3px}

/* nav */
.topbar{left:0;top:0;width:1200px;height:70px;background:var(--black)}
.brand-badge{left:146px;top:5px;width:92px;height:92px;border-radius:50%;background:var(--black);display:flex;align-items:center;justify-content:center;text-align:center;color:var(--blue-bright);font-size:10px;font-weight:700;line-height:1.2;z-index:3}
.nav{left:320px;top:43px;display:flex;gap:30px;color:var(--white);font-size:10px;font-weight:700;z-index:3}
.nav-cta{left:946px;top:35px;width:102px;height:30px;background:var(--blue);color:var(--white);z-index:3}

/* hero */
.hero{left:0;top:70px;width:1200px;height:485px;background:linear-gradient(180deg,#2f5f93 0%,#4f7fae 30%,#3f6f3a 55%,#5d8e2e 100%)}
.hero-title{left:180px;top:178px;width:464px;text-align:center;color:var(--white);font-size:60px;line-height:60px}
.hero-sub{left:232px;top:362px;width:360px;text-align:center;color:var(--white);font-size:11px;line-height:18px;font-weight:700}
.hero-read{left:308px;top:409px;width:102px;height:29px;background:var(--white);color:var(--ink)}
.hero-contact{left:413px;top:409px;width:102px;height:29px;background:var(--blue);color:var(--white)}
.slide-count{left:955px;top:455px;color:var(--white);font-size:38px;font-weight:700}
.slide-count span{font-size:16px;opacity:.6}

.intro-photo{left:156px;top:458px;width:192px;height:192px;border-radius:50%;border:5px solid var(--white);background:radial-gradient(circle at 40% 45%,#e6d7c9,#9b8a79);z-index:2}
.scroll-tab{left:551px;top:522px;width:96px;height:48px;border-radius:48px 48px 0 0;background:var(--white);display:flex;justify-content:center;padding-top:14px}

.intro-title{left:0;top:628px;width:1200px;text-align:center;font-size:37px;line-height:41px}
.intro-title .accent{color:var(--blue)}
.intro-text{left:357px;top:722px;width:486px;text-align:center;font-size:11px;line-height:18px;color:var(--muted)}

/* about */
.about-art{left:200px;top:814px;width:447px;height:417px;border-radius:50%;background:radial-gradient(circle,#3d7fd0 0%,#2f6fc0 55%,rgba(47,111,192,0) 72%)}
.about-kicker{left:679px;top:853px;font-size:37px;color:var(--blue)}
.about-title{left:679px;top:893px;font-size:37px;line-height:41px;color:var(--ink)}
.about-text{left:679px;top:984px;width:310px;font-size:11px;line-height:18px;color:var(--muted)}
.about-text p+p{margin-top:12px}
.about-btn{left:679px;top:1161px;width:102px;height:29px;background:var(--black);color:var(--white)}

/* services */
.services{left:0;top:1280px;width:1200px;height:606px;background:radial-gradient(ellipse at 50% 55%,#3d95f2 0%,#2f78d0 45%,#2560aa 100%)}
.services-title{left:0;top:1338px;width:1200px;text-align:center;color:var(--white);font-size:40px}
.services-sub{left:370px;top:1388px;width:460px;text-align:center;color:var(--white);font-size:11px;line-height:18px}
.service{position:absolute;top:1462px;width:198px;text-align:center;color:var(--white);font-size:14px;font-weight:700;line-height:18px}
.service .photo{width:198px;height:198px;border-radius:50%;margin-bottom:20px}
.arrows{left:540px;top:1764px}

/* serve */
.serve-title{left:0;top:1946px;width:1200px;text-align:center;font-size:40px}
.serve-title .accent{color:var(--blue)}
.card{position:absolute;top:2029px;width:215px;height:238px;background:var(--white);border-radius:8px;box-shadow:var(--card-shadow);text-align:center;padding-top:14px}
.card .icon{width:74px;height:74px;border-radius:50%;margin:0 auto 14px;display:flex;align-items:center;justify-content:center}
.card h3{font-family:'Italiana',serif;font-weight:400;font-size:19px;line-height:22px}
.card p{font-size:10px;line-height:17px;color:var(--muted);margin:8px auto 0;width:160px}
.card .bar{position:absolute;left:85px;bottom:-4px;width:44px;height:4px;background:var(--blue)}
.dark{background:var(--blue-deep)}
.bright{background:var(--blue-bright)}

/* mission */
.mission{left:0;top:2352px;width:1200px;height:618px;background:var(--black)}
.ghost-word{left:0;top:2390px;width:1200px;text-align:center;font-size:86px;color:#1b1b1b;white-space:nowrap}
.mission-photo{left:448px;top:2461px;width:306px;height:424px;border-radius:10px 10px 0 0;background:linear-gradient(180deg,#e9e5e0,#b9c6cc 60%,#8ea7b0)}
.mv-title{top:2520px;color:var(--white);font-size:40px}
.mv-text{top:2575px;width:255px;color:var(--white);font-size:11px;line-height:18px}
.mv-text p+p{margin-top:12px}
.mission-left{left:170px;text-align:right}
.vision-right{left:776px}
.band-word{left:0;top:2820px;width:1200px;text-align:center;color:var(--white);font-size:64px;white-space:nowrap}

/* partners */
.partners-title{left:0;top:3032px;width:1200px;text-align:center;font-size:40px}
.partner{position:absolute;width:218px;height:77px;border:2px solid #cfcfcf;border-radius:6px;display:flex;align-items:center;justify-content:center}
.partner i{display:block;width:96px;height:22px;border-radius:11px;background:#d8d8d8}

/* contact */
.contact-bg{left:0;top:3319px;width:1200px;height:764px;background:linear-gradient(180deg,#fbf7f3 0%,#efe6dd 40%,#e7d8ca 70%,#cbd6e6 100%)}
.contact-card{left:616px;top:3358px;width:375px;height:442px;border-radius:12px;background:linear-gradient(180deg,#2f78d8,#2a68bf);color:var(--white)}
.contact-card h2{position:absolute;left:0;top:52px;width:375px;text-align:center;font-size:40px}
.contact-card .lead{position:absolute;left:40px;top:107px;width:295px;text-align:center;font-size:11px;line-height:18px}
.field{position:absolute;height:38px;border:1px solid rgba(255,255,255,.8);border-radius:19px;font-size:11px;padding:12px 18px}
.submit{left:137px;top:337px;width:102px;height:28px;background:var(--black);color:var(--white)}
.get-touch{left:1040px;top:3430px;transform-origin:0 0;transform:rotate(90deg);font-size:40px;white-space:nowrap;color:var(--ink);letter-spacing:2px}

/* footer */
.footer{left:0;top:4070px;width:1200px;height:313px;background:linear-gradient(180deg,rgba(29,79,149,.0) 0%,#1d4f95 25%,#12305c 100%)}
.footer-brand{left:190px;top:4210px;width:175px;text-align:center;color:var(--blue-bright);font-size:22px;font-weight:700;line-height:24px}
.footer-brand small{display:block;font-size:8px;letter-spacing:1px;color:#9fbde6}
.footer-brand .mark{width:40px;height:40px;border-radius:50%;background:#9fbde6;margin:0 auto 12px}
.foot-head{top:4118px;color:var(--white);font-size:28px}
.foot-list{list-style:none;color:var(--white);font-size:10px}
.foot-list li{position:relative;padding-left:18px;margin-bottom:14px;line-height:15px}
.foot-list li::before{content:"";position:absolute;left:0;top:3px;width:0;height:0;border-left:8px solid var(--white);border-top:5px solid transparent;border-bottom:5px solid transparent}
.footer-rule{left:146px;top:4332px;width:908px;height:1px;background:rgba(255,255,255,.35)}
.copyright{left:0;top:4355px;width:1200px;text-align:center;color:var(--white);font-size:10px}
</style>
</head>
<body>

<!-- navigation -->
<div class="abs topbar"></div>
<div class="abs brand-badge">AMBER<br>CREST</div>
<nav class="abs nav"><span>HOME</span><span>ABOUT US</span><span>WHO WE SERVE</span><span>SERVICES</span><span>MISSION &amp; VISION</span><span>COMMUNITY PARTNERS</span></nav>
<div class="btn nav-cta">CONTACT US</div>

<!-- hero -->
<div class="abs hero" role="img" aria-label="Smiling woman meditating cross-legged on a grassy field under a blue sky"></div>
<h1 class="abs display hero-title">Helping Those<br>Who Help<br>Others</h1>
<p class="abs hero-sub">Suspendisse eleifend rutrum turpis, ac consecteturleo ornare id. Sed placerat feugiat sapien</p>
<div class="btn hero-read">READ MORE</div>
<div class="btn hero-contact">CONTACT US</div>
<div class="abs slide-count">01/<span>02</span></div>

<div class="abs intro-photo" role="img" aria-label="Counsellor sitting with a young mother holding her baby"></div>
<div class="abs scroll-tab">
  <svg width="20" height="40" viewBox="0 0 20 40" fill="none" stroke="#2f6fc0" stroke-width="1.5"><rect x="3" y="1" width="14" height="22" rx="7"/><line x1="10" y1="6" x2="10" y2="11"/><line x1="10" y1="26" x2="10" y2="38"/><polyline points="6,34 10,38 14,34"/></svg>
</div>

<h2 class="abs display intro-title">Fusce sit amet gravida mauris,<br><span class="accent">nec commodo justo</span></h2>
<p class="abs intro-text">Curabitur rutrum lorem at tempus rhoncus. Cras sit amet magna non metus fringilla faucibus quis viverra ipsum. Cras sagittis sem at ligula viverra consectetur. Aliquam quis odio pretium, laoreet nunc ac, blandit arcu. Phasellus bibendum mi vel odio pretium, at hendrerit sem scelerisque.</p>

<!-- about -->
<div class="abs about-art" role="img" aria-label="Large brand emblem artwork in blue"></div>
<div class="abs display about-kicker">About</div>
<h2 class="abs display about-title">Amber Crest Health<br>&amp; Wellness Group</h2>
<div class="abs about-text">
  <p>Duis lobortis dolor velit, efficitur vestibulum neque vulputate id. Nam eleifend, libero in mattis lacinia, tortor lectus ullamcorper eros, sed cursus lectus ante in nisl. Aenean cursus efficitur justo non efficitur. Nullam ultrices volutpat metus, sed aliquam felis euismod a.</p>
  <p>Ut vehicula scelerisque sapien et ornare. Etiam pulvinar ut ante ac pretium. Phasellus ut feugiat enim. Pellentesque a consequat quam.</p>
</div>
<div class="btn about-btn">READ MORE</div>

<!-- services -->
<section class="abs services"></section>
<h2 class="abs display services-title">Our Services</h2>
<p class="abs services-sub">Suspendisse imperdiet cursus sagittis. Maecenas nibh erat, rutrum a est at, dignissim dictum augue. Phasellus at metus auctor, pharetra quam in, malesuada ex.</p>
<div class="service" style="left:168px"><div class="photo" role="img" aria-label="Therapist in session with a distressed man on a sofa" style="background:linear-gradient(135deg,#d9d4cc,#8c8680)"></div>Mental<br>Health Therapy</div>
<div class="service" style="left:388px"><div class="photo" role="img" aria-label="Responders practising CPR on a training manikin" style="background:linear-gradient(135deg,#b9c7c1,#6d7f78)"></div>Trauma &amp; First Responder<br>Support</div>
<div class="service" style="left:607px"><div class="photo" role="img" aria-label="Hands applying a salt scrub to a back" style="background:linear-gradient(135deg,#c9b9c2,#8c7a86)"></div>Salt Therapy</div>
<div class="service" style="left:827px"><div class="photo" role="img" aria-label="Woman using a massage gun on her shoulder" style="background:linear-gradient(135deg,#f1ece8,#a89a90)"></div>Sound &amp; Vibration<br>Therapy</div>
<svg class="abs arrows" width="120" height="40" viewBox="0 0 120 40" fill="none" stroke="#fff" stroke-width="1.5"><circle cx="34" cy="20" r="18"/><line x1="4" y1="20" x2="48" y2="20"/><polyline points="10,14 4,20 10,26"/><circle cx="86" cy="20" r="18"/><line x1="72" y1="20" x2="116" y2="20"/><polyline points="110,14 116,20 110,26"/></svg>

<!-- who we serve -->
<h2 class="abs display serve-title">Who <span class="accent">We Serve</span></h2>
<div class="card" style="left:143px"><div class="icon dark"><svg width="36" height="36" viewBox="0 0 36 36" fill="none" stroke="#fff" stroke-width="1.6"><circle cx="18" cy="18" r="9"/><line x1="18" y1="13" x2="18" y2="23"/><line x1="13" y1="18" x2="23" y2="18"/></svg></div><h3>Vestibulum ante<br>ipsum primis</h3><p>Ut vehicula scelerisque sapien et ornare. Etiam pulvinar ut ante ac pretium.</p><span class="bar"></span></div>
<div class="card" style="left:374px"><div class="icon bright"><svg width="36" height="36" viewBox="0 0 36 36" fill="none" stroke="#fff" stroke-width="1.6"><circle cx="18" cy="14" r="5"/><path d="M8 28c3-6 17-6 20 0"/></svg></div><h3>Phasellus at metus<br>auctor</h3><p>Vestibulum ante ipsum primis in faucibus orci luctus et ultrices</p><span class="bar"></span></div>
<div class="card" style="left:604px"><div class="icon dark"><svg width="36" height="36" viewBox="0 0 36 36" fill="none" stroke="#fff" stroke-width="1.6"><path d="M18 27s-9-5-9-11a5 5 0 0 1 9-3 5 5 0 0 1 9 3c0 6-9 11-9 11z"/></svg></div><h3>Aliquam quis<br>odio pretium</h3><p>Nam eleifend, libero in mattis lacinia, tortor lectus ullamc orper eros,</p><span class="bar"></span></div>
<div class="card" style="left:835px"><div class="icon bright"><svg width="36" height="36" viewBox="0 0 36 36" fill="none" stroke="#fff" stroke-width="1.6"><polyline points="5,19 12,19 15,13 19,24 22,17 31,17"/></svg></div><h3>Nullam sit amet<br>eros ultricies,</h3><p>Donec vel congue erat. Pellentesque consectetur pulvinar</p><span class="bar"></span></div>

<!-- mission & vision -->
<section class="abs mission"></section>
<div class="abs display ghost-word">Amber Crest Health &amp; Wellness</div>
<div class="abs mission-photo" role="img" aria-label="Physiotherapist adjusting a seated woman's neck and shoulder"></div>
<h2 class="abs display mv-title mission-left" style="width:255px">Mission</h2>
<div class="abs mv-text mission-left">
  <p>Nam eleifend, libero in mattis lacinia, tortor lectus ullamcorper eros, sed cursus lectus ante in nisl. Aenean cursus efficitur justo non efficitur. Nullam ultrices volutpat metus, sed aliquam felis euismod a.</p>
  <p>Ut vehicula scelerisque sapien et ornare. Etiam pulvinar ut ante ac pretium. Phasellus ut feugiat enim. .</p>
</div>
<h2 class="abs display mv-title vision-right">Vision</h2>
<div class="abs mv-text vision-right">
  <p>Morbi posuere ex eget libero tempus, sceler isque aliquam nulla dapibus. Nullam sit amet eros ultricies, blandit mauris id, tincidunt leo. Suspendisse imperdiet cursus sagittis. Maecenas nibh erat, rutrum a est at, dignissim dictum augue.</p>
  <p>Phasellus at metus auctor, pharetra quam in, malesuada ex. Sed non ullamcorper dolor, at elementum arcu.</p>
</div>
<div class="abs display band-word">Amber Crest Health &amp; Wellness</div>

<!-- partners -->
<h2 class="abs display partners-title">Community Partners</h2>
<div class="partner" style="left:146px;top:3108px"><i></i></div>
<div class="partner" style="left:373px;top:3108px"><i></i></div>
<div class="partner" style="left:601px;top:3108px"><i></i></div>
<div class="partner" style="left:827px;top:3108px"><i></i></div>
<div class="partner" style="left:146px;top:3198px"><i></i></div>
<div class="partner" style="left:373px;top:3198px"><i></i></div>
<div class="partner" style="left:601px;top:3198px"><i></i></div>
<div class="partner" style="left:827px;top:3198px"><i></i></div>

<!-- contact -->
<div class="abs contact-bg" role="img" aria-label="Smiling woman relaxing on a spa massage table with a flower in her hair and candles"></div>
<div class="abs contact-card">
  <h2 class="display">Contact Us</h2>
  <p class="lead">Duis et enim et diam rhoncus pulvinar. In in urna volutpat, aliquet enim a, auctor lectus. Nam consectetur viverra nisi.</p>
  <div class="field" style="left:22px;top:184px;width:163px">Name</div>
  <div class="field" style="left:189px;top:184px;width:164px">Email</div>
  <div class="field" style="left:22px;top:232px;width:331px">Phone Number</div>
  <div class="field" style="left:22px;top:282px;width:331px;height:54px;border-radius:12px">Message</div>
  <div class="btn submit" style="top:345px">SUBMIT</div>
</div>
<div class="abs display get-touch">GET IN TOUCH</div>

<!-- footer -->
<footer class="abs footer"></footer>
<div class="abs footer-brand"><div class="mark"></div>AMBER CREST<small>HEALTH &amp; WELLNESS GROUP</small></div>
<h3 class="abs display foot-head" style="left:509px">Quick Link</h3>
<ul class="abs foot-list" style="left:509px;top:4178px">
  <li>Home</li><li>Who We Are</li><li>Our Classess</li><li>Contact Us</li><li>Nursery Insights</li>
</ul>
<h3 class="abs display foot-head" style="left:751px">Contact Info</h3>
<ul class="abs foot-list" style="left:751px;top:4178px;width:270px">
  <li>Address: Vivamus ac leo mollis, mollis ligula nec, euismod ante. Ut cursus nisl leo, in vari us urna maximus eu.</li>
  <li>Email: hello@ambercrestwellness.example</li>
  <li>Phone Number: 555 010 2846</li>
</ul>
<div class="abs footer-rule"></div>
<p class="abs copyright">Copyright © 2025 Amber Crest Health &amp; Wellness Group. All rights reserved.</p>

</body>
</html>
```